Zelno Vigor Iron Tempo Multi Vitamin Label Design

We need a label design for our Sports Performance Daily Multi Vitamin specially created and branded for our Zelno Vigor line for the University of Calvoria. The feel is edgy, sports nutrition. Two logos need to be incorporated... Zelno and the Collective Logo attached. The colors should be the official colors of the University of Calvoria. The font may also be the Georgia font... or the Zelno font. Or any font. A hydration product will also be created later on...so this label design may be used on many products. Please utilize the collective logo similar to the use in the attached photo. No official trademark items from the University of Calvoria should be used. Attached is also an image if the bottle (white) that will be used for the vitamin. Please use red, black, grey, white. We are looking for the front design only right now and once selected, will work on the nutrition/back label portion with the artist.

```html
<!DOCTYPE html>
<html lang="en">
<head>
<meta charset="utf-8">
<title>Zelno Vigor – Iron Tempo Multivitamin Label</title>
<link rel="stylesheet" href="https://fonts.googleapis.com/css2?family=Montserrat:wght@300;500;700;800&display=swap">
<style>
  :root {
    --red-deep: #8c0a23;
    --red-main: #a50f2d;
    --red-light: #c9354f;
    --red-rose: #b23a52;
    --black: #1e1e1e;
    --white: #f2f3f4;
    --grey: #d9dadc;
    --page: #ffffff;
  }
  * { margin: 0; padding: 0; box-sizing: border-box; }
  html, body { width: 1200px; height: 1200px; overflow: hidden; background: var(--page); }
  body { position: relative; font-family: "Montserrat", sans-serif; color: var(--white); }

  .label {
    position: absolute; left: 176px; top: 50px; width: 847px; height: 1100px; overflow: hidden;
    background:
      linear-gradient(135deg, transparent 0 62%, rgba(60,0,12,0.18) 62% 100%),
      linear-gradient(90deg, var(--red-main) 0%, var(--red-light) 20%, var(--red-main) 38%, var(--red-deep) 60%, var(--red-rose) 85%, var(--red-deep) 100%);
  }
  .label::before {
    content: ""; position: absolute; inset: 0;
    background: linear-gradient(135deg, transparent 0 55%, rgba(255,255,255,0.06) 55% 100%);
  }

  .brand-name {
    position: absolute; left: 58px; top: 62px;
    font-weight: 800; font-size: 96px; letter-spacing: 0.02em; color: var(--white);
  }
  .partner-badge { position: absolute; left: 612px; top: 58px; width: 190px; height: 190px; }

  .title-panel {
    position: absolute; left: 165px; top: 322px; width: 518px; height: 522px;
    background: var(--black);
  }
  .title-panel__brush {
    position: absolute; left: 38px; top: 560px; width: 132px; height: 210px;
    background: var(--black); opacity: 0.95;
  }
  .title-panel__brush--right {
    left: 683px; top: 430px; width: 160px; height: 130px;
  }

  .product-name { position: absolute; left: 0; right: 0; text-align: center; font-weight: 800; line-height: 1; color: var(--grey); }
  .product-name--first { top: 345px; font-size: 150px; letter-spacing: 0.01em; }
  .product-name--second { top: 478px; font-size: 98px; }

  .product-type {
    position: absolute; left: 0; right: 0; top: 568px; text-align: center;
    font-weight: 500; font-size: 46px; letter-spacing: 0.22em; padding-left: 0.22em; color: var(--white);
  }
  .product-claim {
    position: absolute; left: 0; right: 0; top: 624px; text-align: center;
    font-weight: 700; font-size: 27px; color: var(--white);
  }
  .quality {
    position: absolute; left: 0; right: 0; top: 700px; text-align: center;
    font-weight: 300; font-size: 38px; letter-spacing: 0.02em; color: var(--white);
  }
  .quality__stars { position: absolute; left: 335px; top: 752px; width: 180px; height: 30px; }

  .footer {
    position: absolute; left: 0; right: 0; top: 988px;
    display: flex; justify-content: center; align-items: center; gap: 16px;
  }
  .footer__count { text-align: center; font-weight: 700; line-height: 1; color: var(--white); }
  .footer__count strong { display: block; font-size: 36px; font-weight: 800; }
  .footer__count span { display: block; font-size: 21px; letter-spacing: 0.04em; }
  .footer__rule { width: 2px; height: 62px; background: var(--white); }
  .footer__kind { font-weight: 500; font-size: 17px; letter-spacing: 0.32em; line-height: 1.35; color: var(--white); }
</style>
</head>
<body>
  <main class="label">
    <div class="brand-name">Zelno</div>

    <svg class="partner-badge" viewBox="0 0 190 190" role="img" aria-label="Collective partner badge">
      <circle cx="95" cy="95" r="88" fill="var(--black)"/>
    </svg>

    <div class="title-panel__brush" role="img" aria-label="Black brush stroke"></div>
    <div class="title-panel__brush title-panel__brush--right" role="img" aria-label="Black brush stroke"></div>
    <div class="title-panel"></div>

    <h1 class="product-name product-name--first">IRON</h1>
    <h1 class="product-name product-name--second">TEMPO</h1>
    <p class="product-type">MULTIVITAMIN</p>
    <p class="product-claim">SUPPORT SPORT PERFORMANCE</p>
    <p class="quality">PREMIUM QUALITY</p>
    <svg class="quality__stars" viewBox="0 0 180 30" aria-hidden="true" fill="var(--white)">
      <defs><path id="star" d="M15 2l3.8 8.3 9 1-6.7 6.1 1.9 8.9L15 21.8 7 26.3l1.9-8.9L2.2 11.3l9-1z"/></defs>
      <use href="#star" x="0"/><use href="#star" x="37"/><use href="#star" x="74"/><use href="#star" x="111"/><use href="#star" x="148"/>
    </svg>

    <div class="footer">
      <div class="footer__count"><strong>90</strong><span>TABLETS</span></div>
      <div class="footer__rule"></div>
      <div class="footer__kind">DIETARY<br>SUPLEMENT</div>
    </div>
  </main>
</body>
</html>
```